Las Vegas Themed Video & Messaging Quodra App

We have designed an Quodra app that allows people to share videos and message one another while visiting Las Vegas, Nevada. However, without a simple, compelling design this app will be "just like the rest". This is where you come in.

As a version 1.0 of this app, we want to test the market as inexpensively as possible. There are other screens that we will need to be designed; during development we will be coming back to you for further iterations and enhancements. Consider this contest a paid interview, in other words.

This app will be available to users in the Zembla App Shop. A mockup is attached to the Files section of this brief.

Our mockup is intentionally devoid of almost all styling because we did not want to get in front of your design. The attached mockup exists only to give you a general guide towards the "feel" of the app, but the elements themselves and their placements can (and should) be freely changed by you.

Please be creative; we're excited to see your work!

Requirements
Must have
• Simplicity is the focus. We'd like to see only a few screens from you to judge your work:

• The home screen.
• The messaging screen.
• A screen that records a video.

Nice to have
• A clean, contemporary design:

• Beautiful typography.
• A "flat-ish" design, avoiding skeuomorphism.

```html
<!DOCTYPE html>
<html lang="en">
<head>
<meta charset="utf-8">
<title>Vegas Video &amp; Messaging App Screens</title>
<link href="https://fonts.googleapis.com/css2?family=Oswald:wght@500;700&family=Roboto:wght@400;700&display=swap" rel="stylesheet">
<style>
:root{
  --bg:#ffffff;
  --black:#000000;
  --purple:#4e2a78;
  --sunset:#d2552c;
  --orange:#ff8a00;
  --amber:#ffb000;
  --yellow:#ffe400;
  --pink:#e8196e;
  --pink-tag:#ff4fa0;
  --orange-tag:#f29a1a;
  --cyan:#37c4f2;
  --icon:#b24a00;
  --white:#ffffff;
  --key-bg:#f4f5f7;
  --key-dark:#a9b0bb;
  --key-text:#1c1c1c;
}
*{box-sizing:border-box;margin:0;padding:0}
html,body{width:1200px;height:1200px;overflow:hidden;background:var(--bg)}
body{position:relative;font-family:"Roboto",Arial,sans-serif}
.screen{position:absolute;top:279px;width:306px;height:541px;overflow:hidden;background:var(--black)}
.screen--home{left:74px}
.screen--record{left:449px}
.screen--chat{left:832px}

/* shared header */
.app-header{position:absolute;left:0;top:0;width:100%;background:linear-gradient(180deg,var(--purple) 0%,#8a3a5c 55%,var(--sunset) 100%);color:var(--white)}
.header-row{position:absolute;top:14px;left:16px;right:16px;height:30px;display:flex;align-items:center;justify-content:space-between}
.credits{display:flex;align-items:center;gap:4px;font-family:"Oswald",sans-serif;font-weight:500;font-size:16px}
.header-title{font-family:"Oswald",sans-serif;font-weight:700;font-size:24px;letter-spacing:.3px}
.header-title--user{font-family:"Roboto",sans-serif;font-size:17px}
.add{font-size:28px;font-weight:700;line-height:1}

/* home */
.screen--home .app-header{height:111px}
.search{position:absolute;left:45px;top:67px;width:217px;height:21px;border-radius:11px;background:var(--white);color:#777;font-size:9px;display:flex;align-items:center;justify-content:center}
.feed{position:absolute;top:111px;left:0;width:100%}
.feed-item{position:relative;height:66px;background:var(--black);margin-bottom:13px}
.feed-item::after{content:"";position:absolute;left:0;right:0;bottom:-13px;height:13px;background:var(--orange)}
.thumb{position:absolute;left:0;top:0;width:147px;height:66px}
.thumb--party{background:linear-gradient(135deg,#6b4a3a,#c79c7e 50%,#3b2a22)}
.thumb--pool{background:linear-gradient(135deg,#b02a2a,#e9c8b0 50%,#6aa0c8)}
.thumb--strip{background:linear-gradient(180deg,#1a1a3a,#c98a2a 60%,#3a2a1a)}
.thumb--food{background:linear-gradient(135deg,#8a4a1a,#d9a55a 50%,#4a2a12)}
.duration{position:absolute;right:8px;bottom:5px;background:rgba(0,0,0,.55);color:var(--white);font-size:8px;padding:1px 3px;border-radius:3px}
.item-info{position:absolute;left:162px;top:4px;right:8px;color:var(--white)}
.item-title{font-family:"Oswald",sans-serif;font-weight:500;font-size:17px;color:var(--pink);line-height:20px;white-space:nowrap}
.item-by{font-size:5.5px;line-height:7px}
.item-meta{display:flex;justify-content:space-between;font-size:8px;line-height:11px}
.tags{display:flex;gap:4px;margin-top:3px}
.tag{font-size:5.5px;color:var(--white);padding:1px 5px;border-radius:4px;background:var(--orange-tag)}
.tag--pink{background:var(--pink-tag)}
.tab-area{position:absolute;left:0;bottom:0;width:100%;height:127px;background:linear-gradient(180deg,var(--yellow) 0%,var(--amber) 55%,var(--orange) 100%)}
.tab-bar{position:absolute;left:0;right:0;bottom:8px;display:flex;justify-content:space-around}
.tab{display:flex;flex-direction:column;align-items:center;gap:5px;color:var(--icon);font-size:8.5px;width:70px}
.tab svg{height:30px}

/* record */
.viewfinder{position:absolute;inset:0 0 61px 0;background:linear-gradient(180deg,#5e6fa8 0%,#8c6aa0 30%,#c98a88 55%,#a06a70 72%,#1f1a20 100%)}
.rec{position:absolute;left:12px;top:9px;color:var(--white);font-size:8px;font-weight:700;display:flex;align-items:center;gap:4px}
.rec::before{content:"";width:6px;height:6px;border-radius:50%;background:#e11}
.cam-btn{position:absolute;top:6px;height:32px;border-radius:16px;background:rgba(190,200,225,.75);border:1px solid rgba(255,255,255,.6);display:flex;align-items:center;justify-content:center;font-size:15px;color:#1c1c30}
.cam-btn--options{left:115px;width:83px}
.cam-btn--flip{left:231px;width:66px}
.focus-frame{position:absolute;left:62px;top:92px;width:188px;height:270px;border:1px solid rgba(255,255,255,.7)}
.timer{position:absolute;right:14px;top:437px;color:var(--white);font-size:13px;font-weight:700;background:rgba(0,0,0,.35);padding:1px 4px}
.record-bar{position:absolute;left:0;bottom:0;width:100%;height:61px;background:linear-gradient(180deg,var(--amber),var(--orange))}
.last-clip{position:absolute;left:13px;top:14px;width:51px;height:36px;background:linear-gradient(180deg,#6a8acb,#c9a060);border:1px solid var(--white)}
.shutter{position:absolute;left:133px;top:10px;width:42px;height:42px;border-radius:50%;background:var(--yellow);border:2px solid #d48a00;display:flex;align-items:center;justify-content:center}
.shutter::after{content:"";width:16px;height:16px;border-radius:50%;background:#2a1a00;border:3px solid #ffcc00}

/* chat */
.screen--chat{background:linear-gradient(180deg,var(--orange) 0%,var(--amber) 100%)}
.screen--chat .app-header{height:56px}
.screen--chat .header-row{top:13px}
.thread{position:absolute;top:56px;left:0;width:100%}
.message{height:42px;background:var(--black);display:flex;align-items:center;position:relative}
.message + .message{margin-top:9px}
.message:first-child::after{content:"";position:absolute;left:0;right:0;bottom:-9px;height:9px;background:var(--sunset)}
.avatar{width:44px;height:42px;margin-left:27px;background:linear-gradient(180deg,#e9e4de,#b98a6a)}
.msg-body{margin-left:19px}
.msg-user{font-size:9px;color:var(--white)}
.msg-text{font-size:12.5px;margin-top:2px}
.msg-text--them{color:var(--pink-tag)}
.msg-text--me{color:var(--cyan)}
.compose{position:absolute;left:0;top:284px;width:100%;height:57px;background:linear-gradient(180deg,#7d8595,#9aa1ad);display:flex;align-items:center;padding:0 8px;gap:8px}
.compose-plus{color:#3a3f48;font-size:22px;font-weight:700;width:20px;text-align:center}
.compose-field{flex:1;height:26px;background:var(--white);border-radius:3px;color:#999;font-size:13px;display:flex;align-items:center;padding-left:8px}
.compose-send{height:28px;width:61px;border-radius:3px;background:linear-gradient(180deg,#7c8696,#5c6676);color:var(--white);font-size:14px;display:flex;align-items:center;justify-content:center}
.keyboard{position:absolute;left:0;top:341px;width:100%;height:200px;background:linear-gradient(180deg,#a6acb8,#6f7786);padding:8px 2px 0}
.key-row{display:flex;justify-content:center;gap:3.5px;height:34px;margin-bottom:17px}
.key{width:26.5px;background:var(--key-bg);border-radius:4px;box-shadow:0 1px 0 #3a3f48;display:flex;align-items:center;justify-content:center;font-size:20px;font-weight:700;color:var(--key-text)}
.key--fn{background:var(--key-dark);width:38px;font-size:14px;font-weight:400}
.key--space{width:78px;font-size:14px;font-weight:400}
.key--return{width:68px;background:var(--key-dark);color:var(--white);font-size:14px;font-weight:400}
.key-row--mid{padding:0 14px}
.key-row--shift{justify-content:space-between;padding:0 3px}
.key-row--shift .letters{display:flex;gap:3.5px}
</style>
</head>
<body>

<section class="screen screen--home">
  <header class="app-header">
    <div class="header-row">
      <span class="credits">
        <svg width="14" height="17" viewBox="0 0 14 17" fill="none" stroke="#fff" stroke-width="2"><ellipse cx="7" cy="3.5" rx="6" ry="2.5"/><path d="M1 3.5v10c0 1.4 2.7 2.5 6 2.5s6-1.1 6-2.5v-10M1 8.5c0 1.4 2.7 2.5 6 2.5s6-1.1 6-2.5"/></svg>20
      </span>
      <span class="header-title">AppTitle</span>
      <span class="add">+</span>
    </div>
    <div class="search">Search by username or hashtag</div>
  </header>

  <div class="feed">
    <article class="feed-item">
      <div class="thumb thumb--party" role="img" aria-label="Photo of friends at a party"><span class="duration">12:15</span></div>
      <div class="item-info">
        <div class="item-title">Party@Nova</div>
        <div class="item-by">Submitted by jason387</div>
        <div class="item-meta"><span>2345 views</span><span>1 month ago</span></div>
        <div class="tags"><span class="tag">#Great Party</span><span class="tag">#Free Drinks</span></div>
      </div>
    </article>
    <article class="feed-item">
      <div class="thumb thumb--pool" role="img" aria-label="Photo of a group at a pool party"><span class="duration">02:06</span></div>
      <div class="item-info">
        <div class="item-title">Solace Pool</div>
        <div class="item-by">Submitted by jason387</div>
        <div class="item-meta"><span>2345 views</span><span>1 month ago</span></div>
        <div class="tags"><span class="tag tag--pink">#Hot Girls</span><span class="tag tag--pink">#Swimsuit</span></div>
      </div>
    </article>
    <article class="feed-item">
      <div class="thumb thumb--strip" role="img" aria-label="Photo of the Strip at night with a tower and balloon"><span class="duration">02:06</span></div>
      <div class="item-info">
        <div class="item-title">Evening Strip</div>
        <div class="item-by">Submitted by jason387</div>
        <div class="item-meta"><span>2345 views</span><span>1 month ago</span></div>
        <div class="tags"><span class="tag tag--pink">#Lumiere</span><span class="tag">#Vegas Night</span></div>
      </div>
    </article>
    <article class="feed-item">
      <div class="thumb thumb--food" role="img" aria-label="Photo of a seafood buffet with lobster"><span class="duration">02:06</span></div>
      <div class="item-info">
        <div class="item-title">Seafood Buffet</div>
        <div class="item-by">Submitted by jason387</div>
        <div class="item-meta"><span>2345 views</span><span>1 month ago</span></div>
        <div class="tags"><span class="tag tag--pink">#Lumiere</span><span class="tag">#Vegas Night</span></div>
      </div>
    </article>
  </div>

  <nav class="tab-area" role="img" aria-label="Skyline silhouette backdrop behind the tab bar">
    <div class="tab-bar">
      <div class="tab"><svg viewBox="0 0 30 30" width="30"><path fill="#b24a00" d="M15 1l4.2 9 9.8 1-7.3 6.6 2.1 9.7L15 22.3l-8.8 5 2.1-9.7L1 11l9.8-1z"/></svg>NEWEST</div>
      <div class="tab"><svg viewBox="0 0 40 30" width="40"><ellipse cx="20" cy="15" rx="18" ry="10" fill="#b24a00"/><circle cx="20" cy="15" r="7" fill="#ffc000"/><circle cx="20" cy="15" r="4" fill="#b24a00"/></svg>MOST VIEWS</div>
      <div class="tab"><svg viewBox="0 0 32 30" width="32"><rect x="1" y="3" width="30" height="24" fill="none" stroke="#b24a00" stroke-width="3"/><path stroke="#b24a00" stroke-width="2" stroke-dasharray="2 2" d="M3 6h26M3 24h26"/><rect x="6" y="9" width="20" height="12" fill="#b24a00"/></svg>YOUR VIDEOS</div>
      <div class="tab"><svg viewBox="0 0 36 30" width="36" fill="#b24a00"><rect x="1" y="3" width="10" height="10"/><rect x="13" y="3" width="10" height="10"/><rect x="25" y="3" width="10" height="10"/><rect x="1" y="16" width="10" height="10"/><rect x="13" y="16" width="10" height="10"/><rect x="25" y="16" width="10" height="10"/></svg>MORE</div>
    </div>
  </nav>
</section>

<section class="screen screen--record">
  <div class="viewfinder" role="img" aria-label="Live camera view of a curved hotel tower at dusk"></div>
  <span class="rec">REC</span>
  <div class="cam-btn cam-btn--options">Options</div>
  <div class="cam-btn cam-btn--flip">
    <svg width="40" height="22" viewBox="0 0 40 22" fill="none" stroke="#1c1c30" stroke-width="2"><rect x="12" y="5" width="16" height="12" rx="2"/><circle cx="20" cy="11" r="3.5"/><path d="M3 13a9 9 0 0 1 6-9M37 9a9 9 0 0 1-6 9"/><path d="M6 3l3 1-1 3M34 19l-3-1 1-3"/></svg>
  </div>
  <div class="focus-frame"></div>
  <span class="timer">00:12</span>
  <div class="record-bar">
    <div class="last-clip" role="img" aria-label="Thumbnail of the last recorded clip"></div>
    <div class="shutter"></div>
  </div>
</section>

<section class="screen screen--chat">
  <header class="app-header">
    <div class="header-row">
      <span class="credits">
        <svg width="14" height="17" viewBox="0 0 14 17" fill="none" stroke="#fff" stroke-width="2"><ellipse cx="7" cy="3.5" rx="6" ry="2.5"/><path d="M1 3.5v10c0 1.4 2.7 2.5 6 2.5s6-1.1 6-2.5v-10M1 8.5c0 1.4 2.7 2.5 6 2.5s6-1.1 6-2.5"/></svg>20
      </span>
      <span class="header-title header-title--user">Jason668</span>
      <span class="add">+</span>
    </div>
  </header>

  <div class="thread">
    <div class="message">
      <div class="avatar" role="img" aria-label="Profile photo of Jamie0909"></div>
      <div class="msg-body">
        <div class="msg-user">Jamie0909</div>
        <div class="msg-text msg-text--them">Nice bar, where is this?</div>
      </div>
    </div>
    <div class="message">
      <div class="avatar" role="img" aria-label="Profile photo of Jason668"></div>
      <div class="msg-body">
        <div class="msg-user">Jason668</div>
        <div class="msg-text msg-text--me">It's between zz ave and xx rd.</div>
      </div>
    </div>
  </div>

  <div class="compose">
    <span class="compose-plus">+</span>
    <div class="compose-field">Type your message</div>
    <div class="compose-send">Send</div>
  </div>

  <div class="keyboard">
    <div class="key-row"><span class="key">Q</span><span class="key">W</span><span class="key">E</span><span class="key">R</span><span class="key">T</span><span class="key">Y</span><span class="key">U</span><span class="key">I</span><span class="key">O</span><span class="key">P</span></div>
    <div class="key-row key-row--mid"><span class="key">A</span><span class="key">S</span><span class="key">D</span><span class="key">F</span><span class="key">G</span><span class="key">H</span><span class="key">J</span><span class="key">K</span><span class="key">L</span></div>
    <div class="key-row key-row--shift">
      <span class="key key--fn" style="width:36px">⇧</span>
      <span class="letters"><span class="key">Z</span><span class="key">X</span><span class="key">C</span><span class="key">V</span><span class="key">B</span><span class="key">N</span><span class="key">M</span></span>
      <span class="key key--fn" style="width:36px">⌫</span>
    </div>
    <div class="key-row">
      <span class="key key--fn" style="width:32px">123</span>
      <span class="key key--fn" style="width:28px"><svg width="10" height="16" viewBox="0 0 10 16" fill="none" stroke="#fff" stroke-width="1.5"><rect x="2.5" y="1" width="5" height="9" rx="2.5" fill="#fff"/><path d="M1 7a4 4 0 0 0 8 0M5 11v4"/></svg></span>
      <span class="key key--space">space</span>
      <span class="key" style="font-size:16px">@</span>
      <span class="key">.</span>
      <span class="key key--return">return</span>
    </div>
  </div>
</section>

</body>
</html>
```